DWR Logistics Marketing flyer

Good morning, I run a trucking company and I will be needing help setting up a website logo and a marketing flyer or something like that talking about our services and what we can offer to potential new customers who need to ship their product. I need help getting this all together.

Target Market(s)

Transportation customers

Requirements
Must have
• should list our services and contact info
Nice to have
• the Logo on the top

```html
<!DOCTYPE html>
<html lang="en">
<head>
<meta charset="utf-8">
<title>DWR Logistics – Flyer</title>
<link href="https://fonts.googleapis.com/css2?family=Montserrat:wght@400;500;600;700;800&family=Bebas+Neue&display=swap" rel="stylesheet">
<style>
:root{
  --red:#c40a0a;
  --red-deep:#a30606;
  --orange:#f7a24a;
  --ink:#161616;
  --dark:#1e1a1a;
  --line:#9a9a9a;
  --white:#ffffff;
}
*{margin:0;padding:0;box-sizing:border-box}
html,body{width:960px;height:1200px;overflow:hidden;background:var(--white)}
body{font-family:"Montserrat",Arial,sans-serif;color:var(--ink);position:relative}
.abs{position:absolute}

.hero-panel{left:0;top:0;width:565px;height:440px;background:linear-gradient(160deg,var(--red) 0%,var(--red-deep) 100%)}
.hero-strip{left:0;top:440px;width:565px;height:60px;background:linear-gradient(180deg,#4a4a4a,#2e2e2e)}
.warehouse-photo{left:565px;top:0;width:395px;height:560px;background:linear-gradient(160deg,#6a6a6a 0%,#3d3d3d 55%,#2a2a2a 100%)}
.testimonial-panel{left:495px;top:553px;width:465px;height:326px;background:linear-gradient(180deg,var(--red) 0%,var(--red-deep) 100%)}
.truck-photo{left:360px;top:273px;width:600px;height:370px;
  background:linear-gradient(170deg,#fbfbfb 0%,#e6e6e6 55%,#a0a0a0 80%,#2b2b2b 100%);
  clip-path:polygon(175px 0,100% 47px,100% 290px,70% 100%,45% 100%,0 82%,0 25%,120px 12%)}

.brand{left:69px;top:58px;color:var(--white);font-weight:800;font-size:60px;letter-spacing:-1px;line-height:1;display:flex;align-items:center;gap:12px}
.brand .mark{width:28px;height:28px;background:var(--white)}
.brand-sub{left:69px;top:130px;color:var(--ink);font-weight:700;font-size:15px;letter-spacing:6px}

.headline{left:69px;top:162px;color:var(--white);font-weight:800;font-size:54px;line-height:49px;letter-spacing:.5px}
.headline-accent{left:69px;top:258px;color:var(--orange);font-family:"Bebas Neue",Arial,sans-serif;font-size:76px;line-height:66px;letter-spacing:.5px}
.tagline{left:69px;top:332px;width:300px;border-left:6px solid var(--ink);padding-left:12px;color:var(--white);font-size:19px;line-height:26px;font-weight:500}

.summary-title{left:69px;top:506px;font-weight:800;font-size:19px;line-height:23px}
.summary-title .r{color:var(--red)}
.summary-text{left:69px;top:580px;width:305px;font-size:12.5px;line-height:17px;font-weight:500}

.services-bar{left:0;top:667px;width:422px;height:36px;background:var(--dark);color:var(--white);font-weight:800;font-size:19px;line-height:36px;padding-left:69px}
.services-bar .r{color:var(--red)}
.service-grid{left:69px;top:712px;width:392px;display:grid;grid-template-columns:110px 140px 130px;column-gap:6px}
.service{text-align:center;font-size:12.5px;line-height:16px;font-weight:500;padding-top:4px;height:76px}
.service svg{display:block;margin:0 auto 6px;width:34px;height:22px}
.service.top{border-bottom:1px dashed var(--line);margin-bottom:8px}
.service.mid{border-left:1px dashed var(--line);border-right:1px dashed var(--line)}

.awards-bar{left:0;top:894px;width:374px;height:36px;background:var(--red);color:var(--white);font-weight:800;font-size:19px;line-height:36px;padding-left:69px}
.awards-bar .k{color:var(--ink)}
.awards{left:69px;top:943px;width:390px;list-style:none;font-size:12.5px;line-height:16px;font-weight:500}
.awards li{display:flex;gap:6px;margin-bottom:8px}
.awards li::before{content:"";flex:0 0 10px;height:10px;margin-top:3px;border:2px solid var(--red);border-radius:50%}

.contact-title{left:67px;top:1014px;font-weight:800;font-size:19px}
.contact-title .r{color:var(--red)}
.contact{font-size:15px;font-weight:600;display:flex;gap:10px}
.contact small{display:block;font-size:13px;font-weight:500}
.ico{flex:0 0 18px;height:18px;border-radius:50%;background:var(--red);display:flex;align-items:center;justify-content:center;margin-top:1px}
.ico svg{width:11px;height:11px}
.contact.side{font-size:12.5px;font-weight:500;gap:8px;line-height:16px}
.contact.side .ico{flex-basis:14px;height:14px}
.contact.side .ico svg{width:9px;height:9px}
.follow{left:261px;top:1139px;font-size:12px;letter-spacing:3px;display:flex;align-items:center;gap:12px}
.follow .dot{width:16px;height:16px;border-radius:50%;background:#3b5ba8}

.testi-title{left:514px;top:667px;color:var(--white);font-weight:800;font-size:19px}
.testi-title .o{color:var(--orange)}
.quote{left:535px;width:359px;border-top:1.5px solid var(--orange);border-right:1.5px solid var(--orange);border-bottom:1.5px solid var(--orange);padding:6px 10px 6px 16px;color:var(--white);font-size:12.5px;line-height:17px;font-weight:500}
.quote b{display:block;color:var(--orange);font-weight:800;margin-top:3px}
.qmark{color:var(--orange);font-family:Georgia,serif;font-size:46px;line-height:1}

.apart-title{left:495px;top:903px;font-weight:800;font-size:19px}
.apart-title .r{color:var(--red)}
.apart-text{left:495px;top:933px;width:395px;font-size:12.5px;line-height:16.5px;font-weight:500}
.customers-title{left:495px;top:1050px;color:var(--red);font-weight:800;font-size:18px;letter-spacing:4px}
.customers{left:495px;top:1096px;width:390px;display:flex;justify-content:space-between;align-items:center}
.customer{font-size:14px;font-weight:700;color:#2a2a2a;display:flex;align-items:center;gap:5px}
.customer i{width:10px;height:10px;border-radius:50%;background:var(--red);display:block}
</style>
</head>
<body>
<div class="abs hero-panel"></div>
<div class="abs hero-strip"></div>
<div class="abs warehouse-photo" role="img" aria-label="Photo of a warehouse interior with steel racking"></div>
<div class="abs testimonial-panel"></div>
<div class="abs truck-photo" role="img" aria-label="Photo of a white semi truck with a curtain-side trailer"></div>

<div class="abs brand"><span class="mark"></span>DWR</div>
<div class="abs brand-sub">LOGISTICS LLC</div>

<h1 class="abs headline">MAXIMIZING<br>EFFICIENCY IN</h1>
<div class="abs headline-accent">TRANSPORTATION</div>
<p class="abs tagline">Your Number One Call for Reliable Transportation Solutions</p>

<h2 class="abs summary-title"><span class="r">SUMMARY OF<br>DWR LOGISTICS LLC'S</span><br>SERVICES &amp; EXPERTISE</h2>
<p class="abs summary-text">Specializing in dry van, reefer, flatbed, &amp; tanker loads, we strive to provide efficient &amp; safe transportation solutions for our customers.</p>

<div class="abs services-bar"><span class="r">DWR LOGISTICS LLC'S</span> SERVICES</div>
<div class="abs service-grid">
  <div class="service top"><svg viewBox="0 0 34 22" fill="none" stroke="#c40a0a" stroke-width="1.5"><rect x="2" y="3" width="20" height="13"/><path d="M22 7h6l4 5v4H22z"/><circle cx="8" cy="18" r="2.5"/><circle cx="26" cy="18" r="2.5"/></svg>Dry van<br>Transportation</div>
  <div class="service top mid"><svg viewBox="0 0 34 22" fill="none" stroke="#c40a0a" stroke-width="1.5"><rect x="2" y="3" width="20" height="13"/><path d="M22 7h6l4 5v4H22z"/><path d="M12 5v9M8 7l8 5M16 7l-8 5"/><circle cx="8" cy="18" r="2.5"/><circle cx="26" cy="18" r="2.5"/></svg>Reefer<br>Transportation</div>
  <div class="service top"><svg viewBox="0 0 34 22" fill="none" stroke="#c40a0a" stroke-width="1.5"><rect x="2" y="4" width="6" height="5"/><rect x="9" y="4" width="6" height="5"/><rect x="16" y="4" width="6" height="5"/><path d="M1 12h22M22 7h6l4 5v4H22z"/><circle cx="8" cy="18" r="2.5"/><circle cx="26" cy="18" r="2.5"/></svg>Flatbed<br>Transportation</div>
  <div class="service"><svg viewBox="0 0 34 22" fill="none" stroke="#c40a0a" stroke-width="1.5"><rect x="2" y="5" width="20" height="10" rx="5"/><path d="M22 7h6l4 5v4H22z"/><circle cx="8" cy="18" r="2.5"/><circle cx="26" cy="18" r="2.5"/></svg>Tanker<br>Transportation</div>
  <div class="service mid"><svg viewBox="0 0 34 22" fill="none" stroke="#c40a0a" stroke-width="1.5"><circle cx="13" cy="6" r="4"/><circle cx="21" cy="6" r="4"/><path d="M6 20v-5a4 4 0 0 1 4-4h14a4 4 0 0 1 4 4v5"/></svg>Solo &amp; team<br>driver services</div>
  <div class="service"><svg viewBox="0 0 34 22" fill="none" stroke="#c40a0a" stroke-width="1.5"><circle cx="17" cy="11" r="9"/><circle cx="17" cy="11" r="5"/><circle cx="17" cy="11" r="1.5"/></svg>Adjusting to<br>customer needs<br>with fleet flexibility</div>
</div>

<div class="abs awards-bar">AWARDS &amp; <span class="k">RECOGNITION</span></div>
<ul class="abs awards">
  <li>RQX Elite Carrier Excellence Award (2 years in a row)</li>
  <li>Number one truck supplier to two major orange juice manufacturers in the US</li>
</ul>

<h2 class="abs contact-title"><span class="r">CONTACT US</span> TODAY!</h2>
<div class="abs contact" style="left:69px;top:1049px"><span class="ico"><svg viewBox="0 0 12 12"><path fill="#fff" d="M2.5 1l2 2-1 1.5a7 7 0 0 0 4 4L9 7.5l2 2-1.5 1.5C5 11 1 7 1 2.5z"/></svg></span><div>555-014-2270<small>(CEO Mark Hollis)</small></div></div>
<div class="abs contact" style="left:69px;top:1103px"><span class="ico"><svg viewBox="0 0 12 12"><path fill="#fff" d="M2.5 1l2 2-1 1.5a7 7 0 0 0 4 4L9 7.5l2 2-1.5 1.5C5 11 1 7 1 2.5z"/></svg></span><div>555-014-2270<small>(CFO Dana Pruitt)</small></div></div>
<div class="abs contact side" style="left:261px;top:1051px"><span class="ico"><svg viewBox="0 0 12 12"><rect x="2" y="3" width="8" height="6" fill="none" stroke="#fff" stroke-width="1.2"/><path d="M2 3l4 3 4-3" fill="none" stroke="#fff" stroke-width="1.2"/></svg></span>dispatch@dwrlogistics.com</div>
<div class="abs contact side" style="left:261px;top:1083px"><span class="ico"><svg viewBox="0 0 12 12"><path fill="#fff" d="M6 1a3.5 3.5 0 0 1 3.5 3.5C9.5 7 6 11 6 11S2.5 7 2.5 4.5A3.5 3.5 0 0 1 6 1z"/></svg></span><div>418 Birch Ln. Oakridge,<br>IN 47190</div></div>
<div class="abs follow">FOLLOW US <span class="dot"></span><span class="dot" style="background:#c8367a"></span><span class="dot" style="background:#1a6fb0"></span></div>

<h2 class="abs testi-title"><span class="o">SOME CUSTOMER</span> TESTIMONIALS</h2>
<span class="abs qmark" style="left:514px;top:700px">“</span>
<blockquote class="abs quote" style="top:709px">DWR Logistics LLC has been a reliable partner for our transportation needs<b>Orchardale Citrus Products</b></blockquote>
<span class="abs qmark" style="left:866px;top:752px">”</span>
<span class="abs qmark" style="left:514px;top:788px">“</span>
<blockquote class="abs quote" style="top:797px">Their efficiency and customer service are unmatched.<b>Sunvale Juice North America</b></blockquote>
<span class="abs qmark" style="left:866px;top:840px">”</span>

<h2 class="abs apart-title"><span class="r">WHAT SETS</span> US APART</h2>
<p class="abs apart-text">When you call you will get either the owner or the CFO, you will not have to wait for approvals and time wasted. We work through the problems to find the right solution then get it executed quickly and effectively. You are not just another number to us you are what makes our company possible, and we value that relationship.</p>
<h2 class="abs customers-title">OUR CUSTOMERS</h2>
<div class="abs customers">
  <span class="customer"><i></i>Orchardale</span>
  <span class="customer">Sunvale</span>
  <span class="customer">Crunchway</span>
  <span class="customer">Aquaterra</span>
</div>
</body>
</html>
```